Dalton Power Supply, Inc. Business Card Design

We are an Electrical Distributor looking for a Modern, Professional Business Card design.

Target Market(s)

Residential Commercial Industrial

Industry/Entity Type

Electrical

Contact Information for Business Card

Dalton Power Supply, Inc.
418 Maple Ridge Lane
Brookvale, NC 27514
555-214-7630
555-214-8842 Fax
daltonpower@brightmail-example.net

```html
<!DOCTYPE html>
<html lang="en">
<head>
<meta charset="utf-8">
<title>Dalton Power Supply, Inc. – Business Card</title>
<link href="https://fonts.googleapis.com/css2?family=Jost:wght@400;600&display=swap" rel="stylesheet">
<style>
  :root {
    --ink: #050505;
    --amber: #f3a21d;
    --paper: #ffffff;
    --stage: #ebe7e1;
  }
  * { margin: 0; padding: 0; box-sizing: border-box; }
  html, body { width: 1200px; height: 1200px; overflow: hidden; }
  body {
    background: var(--stage);
    font-family: "Jost", "Futura", sans-serif;
    position: relative;
  }
  .card {
    position: absolute;
    left: 228px;
    width: 744px;
    height: 439px;
    background: var(--ink);
    overflow: hidden;
    box-shadow: 0 14px 30px rgba(0,0,0,0.25);
  }
  .card--front { top: 101px; }
  .card--back { top: 640px; }
  .card__photo {
    position: absolute;
    left: 0;
    top: 0;
    width: 300px;
    height: 439px;
    background: radial-gradient(circle at 125px 130px, #d9d9d9 0%, #6f6f6f 12%, #262626 32%, var(--ink) 62%);
  }
  .card__shapes {
    position: absolute;
    inset: 0;
    width: 100%;
    height: 100%;
  }
  .card__shapes .band { fill: var(--amber); }
  .brand {
    position: absolute;
    display: flex;
    align-items: center;
    gap: 9px;
    font-weight: 600;
    line-height: 1;
    letter-spacing: 0.2px;
    white-space: nowrap;
  }
  .brand__square {
    width: 0.85em;
    height: 0.85em;
    background: currentColor;
    flex: none;
  }
  .card--front .brand {
    right: 46px;
    top: 82px;
    font-size: 20px;
    color: var(--ink);
  }
  .card--back .brand {
    left: 50%;
    top: 235px;
    transform: translateX(-50%);
    font-size: 25px;
    color: var(--paper);
  }
  .contact {
    position: absolute;
    right: 46px;
    top: 208px;
    text-align: right;
    color: var(--paper);
    font-style: normal;
    font-weight: 400;
    font-size: 18px;
    line-height: 24px;
  }
  .contact__group + .contact__group { margin-top: 22px; }
  .corner-mark {
    position: absolute;
    right: 44px;
    bottom: 40px;
    width: 44px;
    height: 44px;
    background: var(--paper);
  }
</style>
</head>
<body>

  <section class="card card--front" aria-label="Business card front">
    <div class="card__photo" role="img" aria-label="Photograph of a glowing clear light bulb on a black background"></div>
    <svg class="card__shapes" viewBox="0 0 624 368" preserveAspectRatio="none" aria-hidden="true">
      <path class="band" d="M170 0 Q 300 160 624 165 L624 0 Z"/>
      <path class="band" d="M30 368 Q 300 300 624 358 L624 368 Z"/>
    </svg>
    <div class="brand"><span class="brand__square"></span>Dalton Power Supply, Inc.</div>
    <address class="contact">
      <div class="contact__group">
        <p>418 Maple Ridge Lane</p>
        <p>Brookvale, NC 27514</p>
      </div>
      <div class="contact__group">
        <p>555-214-7630</p>
        <p>555-214-8842 Fax</p>
        <p>daltonpower@brightmail-example.net</p>
      </div>
    </address>
  </section>

  <section class="card card--back" aria-label="Business card back">
    <svg class="card__shapes" viewBox="0 0 624 368" preserveAspectRatio="none" aria-hidden="true">
      <path class="band" d="M0 0 L470 0 Q 260 95 0 122 Z"/>
      <path class="band" d="M624 195 Q 360 225 200 368 L624 368 Z"/>
    </svg>
    <div class="brand"><span class="brand__square"></span>Dalton Power Supply, Inc.</div>
    <div class="corner-mark" aria-hidden="true"></div>
  </section>

</body>
</html>
```